Calcutta Flyer

Need a 1 pager flyer to promote our upcoming Brindlewood Stakes Calcutta.
I have attached our flyer from last year to give you some ideas.
This years event is being held at the Harrow Vale Inn (Logo provided) and is being sponsored by Tarwick Turf Partnerships (2 logos provided).
We (Corvale Herons Veterans Club 'The Nest') Logo provided are the Calcutta's host and benefactor to the tune of 10% of the overall money raised.
This years event is on Monday 4th November 2024 @ 6.30PM. All other details on last years flyer are relevant for this years flyer as well.

```html
<!DOCTYPE html>
<html lang="en">
<head>
<meta charset="utf-8">
<title>Brindlewood Stakes Calcutta</title>
<link href="https://fonts.googleapis.com/css2?family=Great+Vibes&family=Bebas+Neue&family=Montserrat:wght@800;900&family=Poppins:wght@300;400;600;700&family=Cinzel:wght@700&family=Oswald:wght@300;400&display=swap" rel="stylesheet">
<style>
  :root {
    --bg: #242424;
    --gold: #b98e64;
    --gold-dark: #7a5a3c;
    --cream: #f3dcc0;
    --ticket-dark: #6e4f33;
    --white: #ffffff;
    --silver: #d6d6d6;
    --text-dark: #231c16;
  }
  * { margin: 0; padding: 0; box-sizing: border-box; }
  html, body { width: 943px; height: 1200px; overflow: hidden; background: var(--bg); }
  .flyer { position: relative; width: 943px; height: 1200px; overflow: hidden;
    background: var(--bg); color: var(--white); font-family: "Poppins", sans-serif; }

  .flag-backdrop { position: absolute; right: 0; top: 0; width: 560px; height: 420px;
    background: radial-gradient(ellipse at 85% 20%, #5a5a5a 0%, #3a3a3a 35%, rgba(36,36,36,0) 70%); }
  .floral-accent { position: absolute; left: 0; top: 245px; width: 165px; height: 230px;
    background: radial-gradient(circle at 35% 50%, rgba(160,120,80,.55), rgba(36,36,36,0) 70%); z-index: 2; }
  .racing-photo { position: absolute; left: 0; top: 334px; width: 371px; height: 866px;
    background: linear-gradient(160deg, #6b6b6b 0%, #8c8c8c 30%, #4d4d4d 60%, #3a3530 85%, #2b2724 100%);
    border-top-right-radius: 60px; z-index: 3; }

  .host-mark { position: absolute; left: 77px; top: 60px; width: 183px; height: 228px;
    display: flex; flex-direction: column; align-items: center; justify-content: center; gap: 12px;
    font-family: "Montserrat", sans-serif; font-weight: 800; color: var(--white); text-align: center; z-index: 4; }
  .host-mark .square { width: 28px; height: 28px; background: var(--white); }
  .host-mark .name { font-size: 32px; line-height: 1; letter-spacing: 1px; }
  .host-mark .club { font-size: 14px; line-height: 1.3; }

  .title { position: absolute; left: 0; top: 0; width: 0; height: 0; }
  .title-script { position: absolute; left: 402px; top: 28px; width: 482px; text-align: center;
    font-family: "Great Vibes", cursive; font-size: 140px; line-height: 1; letter-spacing: 3px;
    color: var(--white); z-index: 5; }
  .title-event { position: absolute; left: 402px; top: 146px; width: 482px; text-align: center;
    font-family: "Bebas Neue", sans-serif; font-size: 104px; line-height: 0.8; letter-spacing: 1px;
    background: linear-gradient(180deg, #f2d3a8 0%, #b98e64 45%, #8a6443 70%, #d6b088 100%);
    -webkit-background-clip: text; background-clip: text; color: transparent; z-index: 4; }
  .title-stakes { position: absolute; left: 402px; top: 236px; width: 482px; text-align: center;
    font-family: "Montserrat", sans-serif; font-weight: 900; font-size: 116px; line-height: 0.75;
    color: var(--silver); letter-spacing: -2px; transform: scaleY(1.6); transform-origin: top center; z-index: 4; }

  .info-band { position: absolute; left: 245px; top: 406px; width: 698px; height: 195px;
    background: linear-gradient(90deg, #b88d63 0%, #c39a70 60%, #d7b58d 85%, #b48a60 100%); z-index: 2; }
  .venue { position: absolute; left: 424px; top: 424px; width: 230px; z-index: 4; }
  .venue .label { font-weight: 300; font-size: 24px; letter-spacing: 7px; color: var(--white); line-height: 1; }
  .venue .place { font-weight: 700; font-size: 28px; line-height: 1; color: var(--text-dark); margin-top: 4px; }
  .venue .mark { margin-top: 14px; width: 162px; text-align: center; font-weight: 600; font-size: 16px;
    letter-spacing: 2px; color: var(--white); line-height: 1.3; }
  .band-divider { position: absolute; left: 664px; top: 428px; height: 150px;
    border-left: 1px dashed rgba(255,255,255,.7); z-index: 4; }
  .sponsor { position: absolute; left: 690px; top: 426px; width: 176px; text-align: center; z-index: 4; }
  .sponsor .label { font-family: "Oswald", sans-serif; font-weight: 300; font-size: 24px; line-height: 1;
    letter-spacing: 2px; color: var(--text-dark); }
  .sponsor .square { width: 34px; height: 34px; background: var(--white); margin: 26px auto 22px; }
  .sponsor .name { font-weight: 600; font-size: 15px; line-height: 1.25; color: var(--white); letter-spacing: 1px; }

  .date-day { position: absolute; left: 415px; top: 648px; font-family: "Cinzel", serif; font-weight: 700;
    font-size: 104px; line-height: 1; color: var(--gold); }
  .date-month { position: absolute; left: 415px; top: 744px; font-family: "Cinzel", serif; font-weight: 700;
    font-size: 40px; line-height: 1; color: var(--white); }
  .date-year { position: absolute; left: 430px; top: 776px; font-family: "Great Vibes", cursive;
    font-size: 104px; line-height: 1; color: var(--white); }
  .time-frame { position: absolute; left: 668px; top: 660px; width: 204px; height: 203px;
    border: 1px solid var(--gold); border-left: none; border-radius: 0 8px 8px 0; }
  .time-frame-lead { position: absolute; left: 590px; top: 862px; width: 80px; border-top: 1px solid var(--gold); }
  .weekday { position: absolute; left: 684px; top: 672px; font-family: "Oswald", sans-serif;
    font-weight: 300; font-size: 58px; line-height: 1; color: var(--white); }
  .draw-label { position: absolute; left: 689px; top: 750px; width: 183px; height: 34px;
    background: var(--gold); font-weight: 400; font-size: 17px;
    letter-spacing: 3px; color: var(--white); display: flex; align-items: center; justify-content: center; }
  .draw-time { position: absolute; left: 684px; top: 798px; font-family: "Bebas Neue", sans-serif;
    font-size: 58px; line-height: 1; color: var(--white); }
  .auction-note { position: absolute; left: 722px; top: 841px; font-weight: 300; font-size: 10px;
    line-height: 1; letter-spacing: 1.5px; color: var(--white); }

  .ticket { position: absolute; left: 410px; top: 920px; width: 319px; height: 78px; }
  .ticket-note { position: absolute; left: 739px; top: 922px; width: 170px; }
  .ticket-note .lead { font-weight: 700; font-size: 19px; line-height: 1.1; color: var(--gold); }
  .ticket-note .body { font-weight: 400; font-size: 12.5px; line-height: 1.25; color: var(--white); }

  .terms { position: absolute; left: 410px; top: 1054px; width: 471px; font-weight: 400; font-size: 14.5px;
    line-height: 1.3; letter-spacing: 2.4px; color: var(--white); white-space: nowrap; }
  .web-bar { position: absolute; left: 410px; top: 1096px; width: 471px; height: 48px;
    background: linear-gradient(90deg, #7a5a3c, #b98e64 50%, #7a5a3c);
    display: flex; align-items: center; justify-content: center;
    font-weight: 600; font-size: 23px; letter-spacing: 3px; color: var(--white); }
</style>
</head>
<body>
<main class="flyer">
  <div class="flag-backdrop" role="img" aria-label="Waving chequered racing flag backdrop"></div>
  <div class="info-band"></div>
  <div class="floral-accent" role="img" aria-label="Soft gold floral decoration"></div>
  <div class="racing-photo" role="img" aria-label="Black and white photo of jockeys racing horses"></div>

  <div class="host-mark">
    <span class="square"></span>
    <span class="name">THE NEST</span>
    <span class="club">CORVALE HERONS<br>VETERANS CLUB</span>
  </div>

  <h1 class="title">
    <span class="title-script">Calcutta</span>
    <span class="title-event">BRINDLEWOOD</span>
    <span class="title-stakes">STAKES</span>
  </h1>

  <section class="venue">
    <p class="label">HELD AT</p>
    <p class="place">THE HARROW<br>VALE INN</p>
    <p class="mark">HARROW VALE<br>INN</p>
  </section>
  <div class="band-divider"></div>
  <section class="sponsor">
    <p class="label">SPONSORED BY</p>
    <div class="square"></div>
    <p class="name">TARWICK TURF<br>PARTNERSHIPS</p>
  </section>

  <div class="date-day">4TH</div>
  <div class="date-month">NOVEMBER</div>
  <div class="date-year">2024</div>
  <div class="time-frame"></div>
  <div class="time-frame-lead"></div>
  <div class="weekday">MONDAY</div>
  <div class="draw-label">DRAW FROM</div>
  <div class="draw-time">@6.30PM</div>
  <div class="auction-note">AUCTION TO FOLLOW</div>

  <svg class="ticket" viewBox="0 0 319 78" aria-label="Tickets $5">
    <path d="M1 9 Q9 9 9 1 H155 V77 H9 Q9 69 1 69 Z" fill="var(--cream)" stroke="var(--gold)" stroke-width="2"/>
    <path d="M155 1 H310 Q310 9 318 9 V69 Q310 69 310 77 H155 Z" fill="var(--ticket-dark)" stroke="var(--gold)" stroke-width="2"/>
    <circle cx="155" cy="39" r="12" fill="var(--bg)"/>
    <text x="76" y="54" text-anchor="middle" font-family="Bebas Neue, sans-serif" font-size="42" fill="var(--text-dark)">TICKETS</text>
    <text x="238" y="58" text-anchor="middle" font-family="Cinzel, serif" font-weight="700" font-size="50" fill="var(--cream)">$5</text>
  </svg>
  <div class="ticket-note">
    <p class="lead">10% OF THE</p>
    <p class="body">overall money raised<br>going to the corvale<br>heron veterans</p>
  </div>

  <p class="terms">FOR TERMS AND CONDITIONS PLEASE VISIT</p>
  <div class="web-bar">www.corvalenest.com.au</div>
</main>
</body>
</html>
```